New website for out outstanding veterinary training center

We already have a beautiful logo with nice colors and we are now looking for a breathtaking modern website to present our training center and future corses held there. A section to book open courses should also be available.

We are planing the realize the website with Wordpress.
The following pages should be available:
- Startpage / Overview
- Page to present the different rooms and seating option
- Page where the rooms can be booked
- Page where recommended accommodation are presented
- Page to present and book corses
- contact page
- Impressum

Target Market(s)

European Union

Industry/Entity Type

Education, Veterinary medicine

Number of Pages Required

5+ page

Font styles to use
Sans Serif

Colors
00AB8E
00BBA5
67D7C9
C6EFE9
E9F9F6

Requirements
Must have
• The website must be clear and easy to read. The colors form the logos should be used for the design.
Should not have
• To playful design. The page is not for a veterinary practice. we are a training center for veterinarians!

```html
<!DOCTYPE html>
<html lang="en">
<head>
<meta charset="utf-8">
<title>Vetcampus – Training Center</title>
<link href="https://fonts.googleapis.com/css2?family=Lilita+One&family=Roboto:wght@400;500&display=swap" rel="stylesheet">
<style>
:root{
  --teal:#1a8f85;
  --teal-dark:#0f5a54;
  --teal-light:#cdeeee;
  --blob:#d3e9f3;
  --ink:#3a2e30;
  --grey:#8c8c8c;
  --text:#5a5a5a;
  --white:#ffffff;
}
*{margin:0;padding:0;box-sizing:border-box}
html,body{width:1200px;height:3718px;overflow:hidden}
body{position:relative;font-family:'Roboto',Arial,sans-serif;color:var(--text);background:var(--white)}
.display{font-family:'Lilita One',sans-serif;color:var(--ink);font-weight:400}
section,header,footer{position:absolute;left:0;width:1200px}
.abs{position:absolute}
.photo{position:absolute}

/* header */
.site-header{top:0;height:70px;background:var(--white);z-index:5}
.nav-link{position:absolute;top:23px;font-family:'Lilita One',sans-serif;font-size:15px;color:var(--ink);text-decoration:none}
.brand-bump{position:absolute;left:505px;top:-60px;width:190px;height:190px;border-radius:50%;background:var(--white)}
.brand{position:absolute;left:540px;top:6px;width:120px;text-align:center}
.brand-dot{width:58px;height:58px;border-radius:50%;background:var(--teal);margin:0 auto 6px}
.brand-name{font-family:'Lilita One',sans-serif;font-size:18px;color:var(--teal-dark)}

/* hero */
.hero{top:70px;height:567px;overflow:hidden}
.hero-blob{position:absolute;left:104px;top:45px;width:440px;height:435px}
.hero-copy{position:absolute;left:159px;top:158px}
.hero-kicker{font-size:30px}
.hero-title-1{font-size:64px;color:var(--grey);line-height:1;margin-top:8px;letter-spacing:1px}
.hero-title-2{font-size:72px;line-height:1;margin-top:2px;letter-spacing:1px}
.btn{display:inline-block;background:var(--teal);color:var(--white);font-family:'Lilita One',sans-serif;border-radius:30px;text-align:center}
.hero .btn{position:absolute;left:160px;top:363px;width:200px;height:50px;line-height:50px;font-size:15px}

/* about */
.about{top:637px;height:523px}
.section-title{font-size:34px}
.body-text{font-size:14px;line-height:23px;color:var(--text)}
.about .section-title{position:absolute;left:606px;top:72px}
.about .body-text{position:absolute;left:606px;width:430px}
.about .btn{position:absolute;left:606px;top:357px;width:203px;height:49px;line-height:49px;font-size:14px}

/* rooms */
.rooms{top:1160px;height:562px;background:var(--teal-light)}
.rooms .section-title{position:absolute;width:1200px;text-align:center;top:63px}
.room-card{position:absolute;top:183px;width:207px;height:315px;background:var(--teal);border-radius:26px;border:2px solid #e6f6f4;text-align:center;color:var(--white)}
.room-photo{position:absolute;left:38px;top:-48px;width:130px;height:106px;border-radius:50%;border:3px solid #e6f6f4}
.room-title{font-family:'Lilita One',sans-serif;font-size:24px;line-height:26px;margin-top:75px;color:var(--white)}
.room-text{font-size:14px;line-height:22px;margin:12px 20px 0;color:#e8f7f5}

/* why */
.why{top:1722px;height:675px;background:linear-gradient(#ffffff 0%,#f2f2f2 55%,#d8d8d8 100%);overflow:hidden}
.why .section-title{position:absolute;width:1200px;text-align:center;top:68px}
.why-label{position:absolute;top:240px;font-size:26px;width:200px;text-align:center}
.why .body-text{position:absolute;left:220px;width:760px;top:293px;text-align:center}

/* testimonial */
.testimonial{top:2397px;height:558px}
.quote-mark{position:absolute;left:159px;top:275px;font-family:'Lilita One',sans-serif;font-size:54px;color:var(--ink);line-height:1}
.quote-text{position:absolute;left:159px;top:328px;width:340px;font-size:19px;line-height:27px;color:#4a4a4a}
.quote-author{position:absolute;left:153px;top:418px;font-size:22px;color:var(--ink)}

/* accommodation */
.accommodation{top:2955px;height:387px;background:#f7f7f7}
.accommodation .section-title{position:absolute;left:606px;top:105px}
.accommodation .body-text{position:absolute;left:606px;top:173px;width:430px}
.frame{position:absolute;background:var(--white);padding:8px;box-shadow:0 4px 14px rgba(0,0,0,.25)}

/* footer */
.site-footer{top:3342px;height:376px;background:var(--teal-dark);color:var(--white)}
.footer-head{position:absolute;top:74px;font-family:'Lilita One',sans-serif;font-size:17px;color:var(--white)}
.footer-text{position:absolute;top:113px;font-size:13px;line-height:21px;color:#e3f1ef}
.footer-list{position:absolute;top:110px;left:381px;font-size:13px;line-height:24.5px;color:#e3f1ef;padding-left:22px}
.insta{position:absolute;width:61px;height:50px}
.newsletter-input{position:absolute;left:758px;top:112px;width:285px;height:49px;border-radius:25px;background:var(--white);font-size:14px;color:#777;padding:16px 26px}
.newsletter-btn{position:absolute;left:760px;top:174px;width:200px;height:48px;line-height:48px;font-size:14px;background:var(--teal)}
.copyright{position:absolute;top:314px;width:1200px;text-align:center;font-size:15px;color:var(--white)}
.copyright span{color:#2fc4b2}
</style>
</head>
<body>

<header class="site-header">
  <div class="brand-bump"></div>
  <nav>
    <a class="nav-link" style="left:159px" href="#">Home</a>
    <a class="nav-link" style="left:231px" href="#">Rooms and Seating</a>
    <a class="nav-link" style="left:391px" href="#">Booking Room</a>
    <a class="nav-link" style="left:735px" href="#">Accommodation</a>
    <a class="nav-link" style="left:877px" href="#">Book Courses</a>
    <a class="nav-link" style="left:1003px" href="#">Contact</a>
  </nav>
  <div class="brand"><div class="brand-dot"></div><div class="brand-name">Vetcampus</div></div>
</header>

<section class="hero">
  <div class="photo" role="img" aria-label="Beagle running across a lawn with a green ball in its mouth" style="left:0;top:0;width:1200px;height:567px;background:linear-gradient(160deg,#7fb3d6 0%,#a9cde3 35%,#8a9a6a 70%,#5c6b3c 100%)"></div>
  <svg class="hero-blob" viewBox="0 0 440 435" aria-hidden="true"><path d="M150 10 C260 -10 330 50 360 110 C420 170 450 250 410 330 C370 420 250 450 170 410 C90 380 10 330 0 220 C-10 110 50 30 150 10Z" fill="var(--blob)"/></svg>
  <div class="hero-copy">
    <div class="display hero-kicker">Welcome To&nbsp; Our</div>
    <div class="display hero-title-1">TRAINING</div>
    <div class="display hero-title-2">CENTER</div>
  </div>
  <a class="btn" href="#">BOOK OPEN COURSES</a>
</section>

<section class="about">
  <div class="photo" role="img" aria-label="Illustrated emblem of a puppy and a kitten sitting inside a teal ring on an open book" style="left:159px;top:43px;width:419px;height:432px;border-radius:50% 50% 30% 30%;background:radial-gradient(circle at 50% 45%,#f4f4f4 0%,#e2e2e2 60%,#1a8f85 61%,#1a8f85 67%,#ffffff 68%)"></div>
  <h2 class="display section-title">About Us</h2>
  <p class="body-text" style="top:133px">Many desktop publishing packages and web page editors now use Lorem Ipsum as their default model text, and a search for 'lorem ipsum' will uncover many web sites still in their infancy. Various versions have evolved over the years,</p>
  <p class="body-text" style="top:240px">Many desktop publishing packages and web page editors now use Lorem Ipsum as their default model text, and a search for 'lorem ipsum' will uncover many web sites still in their infancy. Various versions have evolved over the years,</p>
  <a class="btn" href="#">Share Your Memory</a>
</section>

<section class="rooms">
  <h2 class="display section-title">Rooms And Seating</h2>
  <div class="room-card" style="left:159px">
    <div class="room-photo" role="img" aria-label="Dogs resting on the floor" style="background:linear-gradient(#c9c4bd,#9c8a78)"></div>
    <div class="room-title">Lorem Ipsum<br>Simply</div>
    <p class="room-text">Many desktop publishing packages and web page editors now use Lorem Ipsum as their default model text,</p>
  </div>
  <div class="room-card" style="left:386px">
    <div class="room-photo" role="img" aria-label="Person walking dogs outdoors" style="background:linear-gradient(#d7e3b8,#7f9a5a)"></div>
    <div class="room-title">Lorem Ipsum<br>Simply</div>
    <p class="room-text">Many desktop publishing packages and web page editors now use Lorem Ipsum as their default model text,</p>
  </div>
  <div class="room-card" style="left:611px">
    <div class="room-photo" role="img" aria-label="Woman playing with a dog on the grass" style="background:linear-gradient(#cfe0b0,#6d8f45)"></div>
    <div class="room-title">Lorem Ipsum<br>Simply</div>
    <p class="room-text">Many desktop publishing packages and web page editors now use Lorem Ipsum as their default model text,</p>
  </div>
  <div class="room-card" style="left:836px">
    <div class="room-photo" role="img" aria-label="People sitting together in a lounge" style="background:linear-gradient(#e6dcd6,#a48b86)"></div>
    <div class="room-title">Lorem Ipsum<br>Simply</div>
    <p class="room-text">Many desktop publishing packages and web page editors now use Lorem Ipsum as their default model text,</p>
  </div>
</section>

<section class="why">
  <div class="photo" role="img" aria-label="Black and white photo of a black labrador lying in a grass field" style="left:0;top:360px;width:1200px;height:315px;background:linear-gradient(#e8e8e8 0%,#b8b8b8 40%,#6f6f6f 100%)"></div>
  <svg class="abs" style="left:0;top:0" width="1200" height="675" aria-hidden="true">
    <circle cx="600" cy="330" r="292" fill="none" stroke="#ffffff" stroke-width="14"/>
    <g stroke="var(--teal)" stroke-width="3">
      <line x1="266" y1="186" x2="358" y2="186"/><line x1="417" y1="186" x2="538" y2="186"/>
      <line x1="612" y1="186" x2="752" y2="186"/><line x1="814" y1="186" x2="934" y2="186"/>
    </g>
    <g fill="none" stroke="#333" stroke-width="2">
      <path d="M387 160 L410 168 L410 190 C410 202 398 210 387 214 C376 210 364 202 364 190 L364 168 Z"/>
      <path d="M387 176 L391 184 L399 185 L393 191 L395 199 L387 195 L379 199 L381 191 L375 185 L383 184 Z"/>
      <ellipse cx="573" cy="186" rx="26" ry="20"/>
      <path d="M556 182 C566 176 574 192 588 182 M560 194 C570 188 578 200 590 192"/>
      <path d="M783 212 L772 168 M783 212 L783 166 M783 212 L794 168 M765 176 L760 170 M801 176 L806 170"/>
    </g>
  </svg>
  <h2 class="display section-title">Why Choose Us</h2>
  <div class="display why-label" style="left:282px">Honor</div>
  <div class="display why-label" style="left:480px">Remember</div>
  <div class="display why-label" style="left:697px">Celebrate</div>
  <p class="body-text">Lorem Ipsum is simply dummy text of the printing and typesetting industry. Lorem Ipsum has been the industry's standard dummy text ever since the 1500s, when an unknown printer took a galley of type and scrambled it to make a type specimen book.</p>
</section>

<section class="testimonial">
  <div class="photo" role="img" aria-label="Smiling woman hugging a golden labrador, small round portrait" style="left:159px;top:116px;width:166px;height:151px;border-radius:48% 52% 45% 55%;border:4px solid #fff;box-shadow:0 3px 10px rgba(0,0,0,.2);background:linear-gradient(135deg,#4f6a3a,#d7b27e)"></div>
  <div class="quote-mark">“</div>
  <p class="quote-text">Joy to you for providing our sweet pets with such dignified and&nbsp; professional service.</p>
  <div class="quote-author">- Annika</div>
  <div class="photo" role="img" aria-label="Smiling woman hugging a golden labrador outdoors" style="left:553px;top:53px;width:647px;height:445px;background:linear-gradient(120deg,#2f4526 0%,#4d6a3a 40%,#cfa36e 75%,#3a3a2e 100%)"></div>
</section>

<section class="accommodation">
  <div class="frame" style="left:145px;top:48px;width:215px;height:275px;transform:rotate(-8deg)"><div role="img" aria-label="Woman crouching with a dog on a leash in a park" style="width:100%;height:100%;background:linear-gradient(#6f8f56,#3c4a34)"></div></div>
  <div class="frame" style="left:318px;top:78px;width:228px;height:262px;transform:rotate(2deg)"><div role="img" aria-label="Couple kneeling on grass with two dogs" style="width:100%;height:100%;background:linear-gradient(#7d9a5e,#a89272)"></div></div>
  <h2 class="display section-title">Accomodation</h2>
  <p class="body-text">Many desktop publishing packages and web page editors now use Lorem Ipsum as their default model text, and a search for 'lorem ipsum' will uncover many web sites still in their infancy. Various versions have evolved over the years,</p>
</section>

<footer class="site-footer">
  <div class="footer-head" style="left:159px">About</div>
  <p class="footer-text" style="left:159px;width:205px">Many desktop publishing packages and web page editors now use Lorem Ipsum as their default model text, and a search for 'lorem ipsum' will uncover many web sites still in their infancy.</p>
  <div class="footer-head" style="left:381px">Support</div>
  <ul class="footer-list">
    <li>Home</li><li>Rooms and Seating</li><li>Booking Room</li><li>Accommodation</li><li>Book Courses</li><li>Contact</li>
  </ul>
  <div class="footer-head" style="left:543px">Instagram</div>
  <div class="insta" role="img" aria-label="Pet photo" style="left:543px;top:113px;background:#d9a07a"></div>
  <div class="insta" role="img" aria-label="Pet photo" style="left:609px;top:113px;background:#e3d24a"></div>
  <div class="insta" role="img" aria-label="Pet photo" style="left:675px;top:113px;background:#e6c3a3"></div>
  <div class="insta" role="img" aria-label="Pet photo" style="left:543px;top:168px;background:#6fa6d6"></div>
  <div class="insta" role="img" aria-label="Pet photo" style="left:609px;top:168px;background:#c99467"></div>
  <div class="insta" role="img" aria-label="Pet photo" style="left:675px;top:168px;background:#b58b78"></div>
  <div class="footer-head" style="left:758px">Newsletter Sign Up</div>
  <div class="newsletter-input">Enter Email ID</div>
  <a class="btn newsletter-btn" href="#">Subscribe Newsletter</a>
  <p class="copyright">Copyright©2021 <span>veterinary,</span> All Rights Reserved.</p>
</footer>

</body>
</html>
```